トップページをデザインしていただくために、
・当該企業のコーポレートサイトのURL
・コンセプト/メインターゲット
・サイトマップ
・デザインの参考にしていただきたいURL
を準備しています。

※一部情報は下部記載のURLよりファイルをダウンロードください

◆コンセプト
求職者がこの会社で『心から‘働きたい’』と思える採用WEBサイト
~経営者の想い×従業員の想い~ を魅せるサイト

◆参考URL
https://morikaze82.co.jp/recruit/

◆写真素材について
今回、求人サイトの新規構築に際して、有名プロカメラマンによる人物撮影、職場撮影(建築現場含む)を数日に渡り実施いたします。「写真が生きる」ようなデザインのご提案をいただけると幸いです。

※コーポレートサイトのURL、コンセプトの詳しい内容、サイトマップはお手数おかけしますが、下記にてご確認ください。
URL:https://17.hakobako.jp/0922-7a1f30be94d2c658e01b3f9ad4c7e15b0
パス:5172

デザイナーの皆様のご提案お待ちしております。
決裁者に対し、各提案内容のプレゼンを当社担当者が実施し、当選者を決定させていただきます。任意ではありますが、ご提案に際し、提案内容の簡単なPR資料をパワーポイントかPDFにてご用意いただけると大変ありがたいです。

また、デザインデータではわからない動き(ヘッダ固定やスクロールで何かが出現するなど)があれば、わかるように説明をお願いします。Adobe XDで提案いただいても結構です。
素晴らしい提案ありがとうございます。
もう少しパターンを拝見したく、延長をさせていただきます。

よろしくお願いいたします。

スッキリとしたイメージですが、細部までデザインしていただいた印象です。
何よりもクライアント企業様に気に入っていただいたのが大きなポイントとなりました。

沢山のご提案ありがとうございました。
様々なデザインや考え方に触れることができ、大変勉強になりました。

```html
<!DOCTYPE html>
<html lang="ja">
<head>
<meta charset="utf-8">
<title>緑丘建設 採用サイト</title>
<link rel="stylesheet" href="https://fonts.googleapis.com/css2?family=Montserrat:wght@600;700&family=Noto+Sans+JP:wght@400;500;700&display=swap">
<style>
:root{
  --green:#2f9d47;
  --green-dark:#23803a;
  --ink:#2b2e31;
  --muted:#6a6e72;
  --band:#6d7175;
  --paper:#ffffff;
  --mist:#f1f2f3;
  --sky-top:#8fc3ea;
  --sky-low:#e9f3fb;
}
*{box-sizing:border-box;margin:0;padding:0}
html,body{width:1200px;height:5208px;overflow:hidden}
body{position:relative;font-family:"Noto Sans JP",sans-serif;color:var(--ink);background:var(--paper)}
.abs{position:absolute}
.media{position:absolute}
.en-title{font-family:"Montserrat",sans-serif;font-weight:700;font-size:36px;letter-spacing:2px;color:var(--ink)}
.jp-sub{font-size:13px;color:var(--muted);margin-top:4px}
.btn{position:absolute;display:flex;align-items:center;justify-content:space-between;padding:0 22px;color:#fff;font-size:15px;font-weight:500;background:var(--green)}
.btn svg{width:14px;height:14px}
.brand-name{font-weight:700;color:#fff;font-size:26px;letter-spacing:1px}

/* hero */
.hero{left:0;top:0;width:1200px;height:720px}
.hero .photo{left:0;top:0;width:1200px;height:720px;background:linear-gradient(100deg,#c9d9e6 0%,#b6c9d8 35%,#5d6670 55%,#2f3338 80%,#9aa7b1 100%)}
.logo{left:26px;top:20px;display:flex;align-items:center;gap:10px}
.logo .mark{width:30px;height:30px;background:#fff}
.site-label{left:372px;top:30px;font-family:"Montserrat",sans-serif;font-size:11px;letter-spacing:2px;color:#fff}
.entry{left:960px;top:0;width:112px;height:80px;background:var(--green);color:#fff;font-family:"Montserrat",sans-serif;font-weight:600;font-size:14px;display:flex;align-items:center;justify-content:center}
.menu{left:1072px;top:0;width:128px;height:80px;background:var(--green-dark);color:#fff;display:flex;align-items:center;justify-content:center;gap:10px;font-family:"Montserrat",sans-serif;font-size:13px}
.hero-copy{left:168px;top:92px;color:#fff}
.hero-copy .lead{font-size:18px;font-weight:500;margin-bottom:14px}
.hero-copy h1{font-size:46px;font-weight:700;line-height:1.35}
.news{left:272px;top:620px;width:728px;height:64px;display:flex;background:rgba(255,255,255,.85)}
.news .tag{width:96px;background:var(--green);color:#fff;font-family:"Montserrat",sans-serif;font-weight:700;font-size:15px;display:flex;align-items:center;justify-content:center}
.news .item{flex:1;display:flex;align-items:center;gap:40px;padding:0 28px;font-size:14px;color:var(--ink)}
.news .item time{margin-left:auto;color:var(--muted);font-size:13px}

/* sky (message + company heading) */
.sky{left:0;top:720px;width:1200px;height:880px;background:linear-gradient(180deg,var(--sky-top) 0%,#c4e0f4 45%,var(--sky-low) 100%)}
.message-head{left:140px;top:810px}
.message-body{left:140px;top:890px;width:460px;font-size:14px;line-height:2.3;color:#fff}
.message-body p+p{margin-top:18px}
.group-panel{left:660px;top:800px;width:440px;height:180px;background:#fff;padding:22px 30px;display:grid;grid-template-columns:1fr 1fr 1fr;gap:14px;align-content:start}
.group-panel .sister{font-weight:700;font-size:18px;color:var(--green);text-align:center}
.group-panel .parent{grid-column:1/4;display:flex;align-items:center;justify-content:center;gap:10px;font-weight:700;font-size:26px;color:var(--green);margin-top:12px}
.group-panel .parent span.sq{width:24px;height:24px;background:var(--green)}
.company-head{left:0;top:1370px;width:1200px;text-align:center}
.company-tag{left:0;top:1520px;width:1200px;text-align:center;font-size:20px;font-weight:700}
.company-text{left:0;top:1556px;width:1200px;text-align:center;font-size:13px;line-height:1.9;color:var(--ink)}
.house{left:0;top:1600px;width:1200px;height:480px;background:linear-gradient(180deg,#b8d6ee 0%,#e8ecef 40%,#d9d4cc 75%,#8fa070 100%)}
.band{left:0;top:2080px;width:1200px;height:320px;background:var(--band)}
.band-card{top:2120px;width:480px;height:140px;display:flex;align-items:center;padding-left:40px;color:#fff;font-size:22px;font-weight:700}
.band-card.l{left:80px;background:linear-gradient(90deg,#4b4f53,#8b8680)}
.band-card.r{left:640px;background:linear-gradient(90deg,#e8eaec,#9aa2a8)}
.band-card.r span{color:var(--ink)}

/* work */
.work-head{left:40px;top:2480px}
.work-catch{left:40px;top:2580px;font-size:22px;font-weight:700}
.work-text{left:40px;top:2624px;width:500px;font-size:13px;line-height:2;color:var(--ink)}
.work-right{left:600px;top:2480px;width:600px;height:720px;background:linear-gradient(160deg,#9fc9a8,#3d8f55 60%,#2b6b3f)}
.work-left{left:0;top:2760px;width:600px;height:440px;background:linear-gradient(135deg,#5fae74,#2e7d47)}
.work-btn1{left:180px;top:3080px;width:200px;height:52px;background:var(--green-dark)}
.work-btn2{left:720px;top:3100px;width:200px;height:52px;background:var(--green-dark)}

/* interview */
.interview{left:0;top:3200px;width:1200px;height:1120px;background:var(--mist)}
.interview-head{left:0;top:3400px;width:1200px;text-align:center}
.interview-q{left:0;top:3520px;width:1200px;display:flex;justify-content:center;align-items:center;gap:10px;font-size:18px;font-weight:700}
.interview-q .dot{width:18px;height:18px;border-radius:50%;background:var(--green)}
.interview-lead{left:0;top:3556px;width:1200px;text-align:center;font-size:13px;color:var(--muted)}
.iv-card{top:3640px;width:380px}
.iv-card .photo{position:relative;width:380px;height:320px}
.iv-card .label{position:absolute;left:0;bottom:22px;background:#fff;border-left:6px solid var(--green);padding:8px 18px;font-size:17px;font-weight:700;color:var(--green);line-height:1.5}
.iv-card .name{margin-top:16px;padding-left:14px;font-size:13px;line-height:1.6;color:var(--ink)}
.iv-card .name small{display:block;color:var(--muted);font-size:12px}
.more-iv{left:520px;top:4210px;width:180px;height:50px}

/* recruit */
.recruit-head{left:60px;top:4350px}
.rc-card{top:4490px;width:320px;border-top:4px solid var(--green);padding-top:18px;text-align:center}
.rc-card h3{font-size:19px;font-weight:700}
.rc-card .photo{margin-top:20px;width:320px;height:300px}
.rc-card .btn{position:relative;margin:40px auto 0;width:170px;height:48px}

/* footer */
.footer{left:0;top:5088px;width:1200px;height:120px;background:var(--green);display:flex;align-items:center;justify-content:space-between;padding:0 40px;color:#fff}
.footer .copy{font-size:11px;opacity:.9}
</style>
</head>
<body>

<section class="hero abs">
  <div class="photo media" role="img" aria-label="スーツ姿の社員たちが前を見つめる集合写真"></div>
</section>
<div class="logo abs"><span class="mark"></span><span class="brand-name">緑丘建設</span></div>
<div class="site-label abs">RECRUITING SITE</div>
<a class="entry abs">ENTRY</a>
<div class="menu abs">
  <svg width="22" height="16" viewBox="0 0 22 16"><path d="M0 1h22M0 8h22M0 15h22" stroke="#fff" stroke-width="2"/></svg>MENU
</div>
<div class="hero-copy abs">
  <p class="lead">家は人の幸せをつくるもの。</p>
  <h1>今やりたいことを、<br>かたちにする。</h1>
</div>
<div class="news abs">
  <div class="tag">NEWS</div>
  <div class="item"><span>採用サイトOpen</span><time>2020.05.01</time></div>
</div>

<div class="sky abs" role="img" aria-label="雲の浮かぶ青空"></div>
<div class="message-head abs"><h2 class="en-title" style="color:#fff">MESSAGE</h2><p class="jp-sub" style="color:#fff">採用メッセージ</p></div>
<div class="message-body abs">
  <p>見出しが入ります。見出しが入ります。<br>テキストが入ります。テキストが入ります。テキストが入ります。<br>テキストが入ります。テキストが入ります。<br>テキストが入ります。テキストが入ります。テキストが入ります。</p>
  <p>皆さんのご応募をお待ちしております。</p>
</div>
<div class="group-panel abs">
  <span class="sister">あおば</span><span class="sister">TsuMiKi</span><span class="sister">木楽</span>
  <div class="parent"><span class="sq"></span>緑丘建設</div>
</div>

<div class="company-head abs"><h2 class="en-title">COMPANY</h2><p class="jp-sub">会社を知る</p></div>
<p class="company-tag abs">「満足」「安心」「感動」をお客様と共感。</p>
<p class="company-text abs">緑丘建設は、地域の皆さまの暮らしに寄り添い、住まいづくりを通じて笑顔を届けています。<br>家づくりの喜びを、お客様と共に分かち合う会社です。</p>
<div class="house media" role="img" aria-label="白い外壁と木目アクセントの二階建て住宅"></div>
<div class="band abs"></div>
<div class="band-card l abs" role="img" aria-label="明るいリビングの室内写真"><span>経営理念</span></div>
<div class="band-card r abs" role="img" aria-label="代表者のポートレート"><span>代表メッセージ</span></div>

<div class="work-head abs"><h2 class="en-title">WORK</h2><p class="jp-sub">仕事内容を知る</p></div>
<p class="work-catch abs">全てはお客様の笑顔のために。</p>
<p class="work-text abs">お客様とのコミュニケーションを大切にし、スタッフ間の連携、材料と工程を整えながら、一棟一棟を丁寧に仕上げています。</p>
<div class="work-right media" role="img" aria-label="建築現場でヘルメットを被り作業する社員"></div>
<div class="work-left media" role="img" aria-label="図面と設計道具の写真"></div>
<a class="btn work-btn1">部門紹介<svg viewBox="0 0 14 14"><path d="M4 2l6 5-6 5" fill="none" stroke="#fff" stroke-width="2"/></svg></a>
<a class="btn work-btn2">実績紹介<svg viewBox="0 0 14 14"><path d="M4 2l6 5-6 5" fill="none" stroke="#fff" stroke-width="2"/></svg></a>

<section class="interview abs"></section>
<div class="interview-head abs"><h2 class="en-title">INTERVIEW</h2><p class="jp-sub">社員インタビュー</p></div>
<p class="interview-q abs"><span class="dot"></span>緑丘建設ってどんな会社です！</p>
<p class="interview-lead abs">株式会社緑丘建設で活躍する社員に聞いてみました。仕事のやりがいや会社の雰囲気をご紹介します。</p>

<div class="iv-card abs" style="left:0">
  <div class="photo media" role="img" aria-label="オフィスで微笑む女性社員" style="position:relative;background:linear-gradient(135deg,#d8cfc4,#a99a8a)"><span class="label">明るく<br>アットホームな会社</span></div>
  <p class="name">SHOTA<small>設計部 2015年入社</small></p>
</div>
<div class="iv-card abs" style="left:410px">
  <div class="photo media" role="img" aria-label="眼鏡をかけたスーツ姿の男性社員" style="position:relative;background:linear-gradient(135deg,#c9c4bd,#6f6a66)"><span class="label">個性を大事に<br>動ける会社</span></div>
  <p class="name">RYO<small>営業部 2017年入社</small></p>
</div>
<div class="iv-card abs" style="left:820px">
  <div class="photo media" role="img" aria-label="カラフルな売場に立つ女性社員" style="position:relative;background:linear-gradient(135deg,#e6d27a,#7fb0d8)"><span class="label">お客様のことを一番に<br>考えた安心・住まい会社</span></div>
  <p class="name">AYANO<small>営業部 2018年入社</small></p>
</div>
<a class="btn more-iv abs">MORE<svg viewBox="0 0 14 14"><path d="M4 2l6 5-6 5" fill="none" stroke="#fff" stroke-width="2"/></svg></a>

<div class="recruit-head abs"><h2 class="en-title">RECRUIT</h2><p class="jp-sub">採用情報</p></div>
<div class="rc-card abs" style="left:60px">
  <h3>募集要項</h3>
  <div class="photo" role="img" aria-label="スーツ姿の男性社員" style="background:linear-gradient(135deg,#dfe3e6,#5b6168)"></div>
  <a class="btn">MORE<svg viewBox="0 0 14 14"><path d="M4 2l6 5-6 5" fill="none" stroke="#fff" stroke-width="2"/></svg></a>
</div>
<div class="rc-card abs" style="left:440px">
  <h3>採用Q&amp;A</h3>
  <div class="photo" role="img" aria-label="ノートパソコンで作業する手元" style="background:linear-gradient(135deg,#eceff1,#9aa5ad)"></div>
  <a class="btn">MORE<svg viewBox="0 0 14 14"><path d="M4 2l6 5-6 5" fill="none" stroke="#fff" stroke-width="2"/></svg></a>
</div>
<div class="rc-card abs" style="left:820px">
  <h3>福利厚生</h3>
  <div class="photo" role="img" aria-label="オフィスに立つ女性社員" style="background:linear-gradient(135deg,#f2f2ef,#b9b3ab)"></div>
  <a class="btn">MORE<svg viewBox="0 0 14 14"><path d="M4 2l6 5-6 5" fill="none" stroke="#fff" stroke-width="2"/></svg></a>
</div>

<footer class="footer abs">
  <div style="display:flex;align-items:center;gap:10px"><span style="width:26px;height:26px;background:#fff"></span><span class="brand-name" style="font-size:22px">緑丘建設</span></div>
  <p class="copy">Copyright © 緑丘建設｜本社：〇〇県〇〇市〇〇町1-2-3　All rights reserved.</p>
</footer>

</body>
</html>
```